Modern Yoga Studio Timetable and Flyer Design

We have a comprehensive class timetable and we are wanting to a clean modern look for our Spring timetable.

We require a double sided flyer with our class timetable included.
We would prefer an A5 size (postcard) or DL (1/3 A4).

We would like the final flyer to have.
Side A : Yoga image, logo

Fennel Stretch Hall
address: 4/71 Wexcombe Lane, Pelharton
website: fennelstretch.com.au
mobile: 0471 296 814

Side B: Clear easy to read timetable with a break down of class types and website.

We would also like to have a copy of the timetable itself as a separate jpg or pdf for use on our website to download.

Thank you.
Yours kindly,
Nell

I have attached a sample of another timetable of which I like the look and feel of, however this is just a guide. I've also attached our 'new' schedule in WORD plus uploaded our last design of the front.
Updates

Target Market(s)

Women aged 30-45

Industry/Entity Type

Health And Wellness

Font styles to use
Other font styles liked:
• Brandon Grotesque, Jenna Sue

Colors
6c459b
33a6d7
ffffff

Requirements
Must have
• A definitive colour to decipher between different class types on our timetable. Where each colour represents a different class type. Colours and layouts similar to our website design, see www.fennelstretch.com.au
Nice to have
• I've included a design of another studio whose timetable design I like. One of our own yoga images instead of a stock image.
Should not have
• No dark gridlines between the cells/boxes in the timetables. Please don't use stock yoga images.

```html
<!DOCTYPE html>
<html lang="en">
<head>
<meta charset="utf-8">
<title>Fennel Stretch Hall – Spring Flyer</title>
<link rel="stylesheet" href="https://fonts.googleapis.com/css2?family=Lato:wght@300;400;700;900&display=swap">
<style>
  :root{
    --purple:#6c459b;
    --purple-deep:#4f2a85;
    --blue:#33a6d7;
    --sky:#c9e7f6;
    --navy:#1e2858;
    --white:#ffffff;
    --ink:#2b2540;
    --backdrop:#e7e7ea;

    /* one colour per class type */
    --class-rise:#f0a541;
    --class-vinyasa:#4f2a85;
    --class-slow:#2f93c4;
    --class-pregnancy:#c2489a;
    --class-mum:#8e63c4;
    --class-kids:#2bb39a;
    --class-teens:#1c6f9c;
    --class-flow-restore:#5f7fd0;
    --class-wellness:#a8326f;
    --class-yin-restore:#2f4f86;
    --class-yin:#7cc3e4;
  }
  *{box-sizing:border-box;margin:0;padding:0}
  html,body{width:794px;height:1200px;overflow:hidden;background:var(--backdrop)}
  body{font-family:"Lato",Arial,sans-serif;color:var(--ink);position:relative}

  /* ---------- Side A ---------- */
  .flyer-front{
    position:absolute;left:37px;top:40px;width:720px;height:470px;
    background:var(--white);overflow:hidden;box-shadow:0 6px 18px rgba(0,0,0,.18);
  }
  .front-shape,.front-photo{position:absolute;left:0;top:0;width:720px;height:470px}
  .front-brand{
    position:absolute;right:70px;top:36px;
    font-size:22px;font-weight:400;color:var(--blue);letter-spacing:4px;text-transform:lowercase;
  }
  .front-title{
    position:absolute;right:62px;top:150px;width:300px;text-align:right;
    font-size:50px;font-weight:300;line-height:1.02;color:var(--blue);
  }
  .front-title span{display:block;color:var(--purple-deep);font-size:34px;font-weight:400;letter-spacing:3px}
  .front-contact{position:absolute;right:40px;top:330px;width:290px}
  .front-address{font-size:13px;color:var(--ink);margin-bottom:6px}
  .front-call{
    background:var(--purple);color:var(--white);font-size:19px;font-weight:700;
    padding:5px 12px;margin-bottom:8px;
  }
  .front-web{font-size:13px;letter-spacing:2px;color:var(--ink);text-align:center}

  /* ---------- Side B ---------- */
  .flyer-back{
    position:absolute;left:37px;top:550px;width:720px;height:610px;
    background:var(--white);box-shadow:0 6px 18px rgba(0,0,0,.18);padding:18px 24px 24px;
  }
  .back-brand{text-align:center;font-size:20px;color:var(--blue);letter-spacing:4px;text-transform:lowercase;margin-bottom:14px}
  .back-heading{
    background:var(--purple);color:var(--sky);font-size:21px;font-weight:400;
    padding:9px 16px;margin:0 -24px 14px;letter-spacing:.3px;
  }
  .timetable{width:100%;border-collapse:collapse;table-layout:fixed;font-size:11px}
  .timetable th,.timetable td{height:32px;text-align:center;text-transform:uppercase;border:0}
  .timetable thead th{height:28px;font-size:15px;font-weight:700;color:var(--purple-deep);background:var(--white)}
  .timetable .time{
    width:92px;background:var(--navy);color:var(--white);font-size:14px;font-weight:400;
    border-left:8px solid var(--blue);
  }
  .timetable tbody tr:nth-child(odd) td{background:var(--sky)}
  .timetable tbody tr:nth-child(even) td{background:var(--white)}
  .timetable td.class-slot{color:var(--white);font-weight:700;line-height:1.1;padding:0 3px}
  .timetable tbody tr td.rise{background:var(--class-rise);color:var(--navy)}
  .timetable tbody tr td.vinyasa{background:var(--class-vinyasa)}
  .timetable tbody tr td.slow{background:var(--class-slow)}
  .timetable tbody tr td.pregnancy{background:var(--class-pregnancy)}
  .timetable tbody tr td.mum{background:var(--class-mum)}
  .timetable tbody tr td.kids{background:var(--class-kids)}
  .timetable tbody tr td.teens{background:var(--class-teens)}
  .timetable tbody tr td.flow-restore{background:var(--class-flow-restore)}
  .timetable tbody tr td.wellness{background:var(--class-wellness)}
  .timetable tbody tr td.yin-restore{background:var(--class-yin-restore)}
  .timetable tbody tr td.yin{background:var(--class-yin)}
</style>
</head>
<body>

<section class="flyer-front">
  <svg class="front-shape" viewBox="0 0 720 470" aria-hidden="true">
    <path d="M0 0 H300 C250 80 230 200 290 300 C340 380 430 440 520 470 H0 Z" fill="#6c459b"/>
    <path d="M300 0 C250 80 230 200 290 300 C340 380 430 440 520 470" fill="none" stroke="#33a6d7" stroke-width="9"/>
  </svg>
  <svg class="front-photo" viewBox="0 0 720 470" role="img" aria-label="Photograph of a yoga teacher holding a twisted side-angle pose">
    <defs>
      <linearGradient id="photoTone" x1="0" y1="0" x2="1" y2="1">
        <stop offset="0" stop-color="#c9a07e"/>
        <stop offset=".5" stop-color="#7b4aa5"/>
        <stop offset="1" stop-color="#e8dccd"/>
      </linearGradient>
    </defs>
    <path d="M70 150 Q140 110 220 150 L300 260 Q360 330 440 420 L380 430 Q300 390 250 380 L190 440 L110 440 L150 360 Q100 300 90 230 Z" fill="url(#photoTone)" opacity=".8"/>
  </svg>
  <div class="front-brand">fennel stretch hall</div>
  <h1 class="front-title">Fennel<span>Stretch Hall</span></h1>
  <div class="front-contact">
    <p class="front-address">ADDRESS: 4/71 Wexcombe Lane, Pelharton</p>
    <p class="front-call">CALL US: 0471 296 814</p>
    <p class="front-web">www.fennelstretch.com.au</p>
  </div>
</section>

<section class="flyer-back">
  <div class="back-brand">fennel stretch hall</div>
  <h2 class="back-heading">FENNEL STRETCH SPRING TIMETABLE</h2>
  <table class="timetable">
    <thead>
      <tr><th></th><th>Mon</th><th>Tue</th><th>Wed</th><th>Thur</th><th>Fri</th><th>Sat</th><th></th></tr>
    </thead>
    <tbody>
      <tr><th class="time">5.45AM</th><td></td><td class="class-slot rise">Rise + Shine*</td><td></td><td class="class-slot rise">Rise + Shine*</td><td></td><td></td><td></td></tr>
      <tr><th class="time">9.00AM</th><td></td><td></td><td></td><td></td><td></td><td class="class-slot vinyasa">Vinyasa Flow</td><td class="class-slot yin">Yin</td></tr>
      <tr><th class="time">9.15AM</th><td></td><td class="class-slot vinyasa">Vinyasa Flow</td><td></td><td class="class-slot vinyasa">Vinyasa Flow</td><td></td><td></td><td></td></tr>
      <tr><th class="time">9.30AM</th><td class="class-slot slow">Slow Flow</td><td></td><td></td><td></td><td></td><td class="class-slot pregnancy">Pregnancy*</td><td></td></tr>
      <tr><th class="time">9.30AM</th><td></td><td class="class-slot mum">Mum + Baby*</td><td></td><td class="class-slot mum">Mum + Baby*</td><td></td><td></td><td></td></tr>
      <tr><th class="time">10.30AM</th><td></td><td></td><td></td><td class="class-slot pregnancy">Pregnancy</td><td></td><td class="class-slot vinyasa">Vinyasa Flow</td><td></td></tr>
      <tr><th class="time">11AM</th><td></td><td></td><td class="class-slot kids">Kids 8-12*</td><td class="class-slot kids">Kids 5-7*</td><td></td><td></td><td></td></tr>
      <tr><th class="time">12.15PM</th><td></td><td></td><td class="class-slot teens">Teens 12-16*</td><td></td><td></td><td></td><td></td></tr>
      <tr><th class="time">4.45PM</th><td></td><td></td><td></td><td class="class-slot teens">Teens 12-16*</td><td class="class-slot flow-restore">Flow + Restore</td><td></td><td></td></tr>
      <tr><th class="time">5.00PM</th><td></td><td></td><td></td><td></td><td></td><td></td><td></td></tr>
      <tr><th class="time">6.00PM</th><td class="class-slot pregnancy">Pregnancy*</td><td class="class-slot vinyasa">Vinyasa Flow</td><td class="class-slot slow">Slow Flow</td><td class="class-slot pregnancy">Pregnancy*</td><td></td><td></td><td></td></tr>
      <tr><th class="time">6.15PM</th><td></td><td></td><td></td><td class="class-slot wellness">Women's Wellness*</td><td></td><td></td><td></td></tr>
      <tr><th class="time">7.30PM</th><td class="class-slot vinyasa">Vinyasa Flow</td><td class="class-slot pregnancy">Pregnancy*</td><td class="class-slot yin-restore">Yin + Restore</td><td></td><td></td><td></td><td></td></tr>
    </tbody>
  </table>
</section>

</body>
</html>
```